Local Newspaper Quarterly " Meet The Realtor" print ad

I need a new add made up. This was my last ad:
http://www.harborlinepressads.example/static/pdfs/agents1309/Ar092213%20G10%20006%20Prepress.pdf

I do not really care of Realtor advertisements because they are just so cheesy and rather pompous-like. However, it's a necessary evil
My ads have always been outside of the box and/or visually sharp.
I now have a new company' Voske Real Estate( I will attach a logo) contact info:
Carl Voske
Voske Real Estate
Broker/Owner( this can be somewhere in small print or corner of ad since it's mandatory to have shown
Phone: 304-555-0194
Email: Carl@VoskeRealEstate.Example
VoskeRealEstate.Example
I would like social icons(FL,Chirpr, Pinmosaic! Dwello, Qlink)

Ideas: In my logo font or using the image at the top I envision
Something like:
A
Voske Real Estate
Of Mind
Body of ad?
Images of Charleston WV as a real light back ground
With 3 or 4 customer reviews chosen by you in this site:
http://webcarl.example/think.html

Bottom: contact info and my name in a nice Signature style ??
My agent pic at the bottom right( to be small. I don't want my big head overshadowing the message)

I have yet to think of a tagline for my new company:
I have been thinking of " Luxury Services For All Things Real Estate"

Or nothing at all ??? I don't care for tag lines but then again that's part of the business

Target Market(s)

Higher end homes

Industry/Entity Type

Business

Colors
0f59a5
0392cd
0f0f0f
eaeaea
ffffff

Requirements
Must have
• My logo and colors
Nice to have
• My agent picture and client review.
Should not have
• No typical real estate images like a house or home buyer

```html
<!DOCTYPE html>
<html lang="en">
<head>
<meta charset="utf-8">
<title>Voske Real Estate – Meet The Realtor</title>
<link rel="stylesheet" href="https://fonts.googleapis.com/css2?family=Jost:ital,wght@0,300;0,400;0,500;0,600;1,400&display=swap">
<style>
  :root {
    --brand-blue: #0f59a5;
    --panel-blue: #1270b8;
    --sky-blue: #0392cd;
    --ink: #0f0f0f;
    --band-grey: #3a3d40;
    --light-grey: #eaeaea;
    --white: #ffffff;
  }
  * { box-sizing: border-box; margin: 0; padding: 0; }
  html, body { width: 1200px; height: 922px; overflow: hidden; background: var(--white); }
  body { font-family: "Jost", "Futura", sans-serif; color: var(--white); }

  .ad { position: relative; width: 1200px; height: 922px; background: var(--white); }

  .masthead { position: absolute; left: 0; top: 0; width: 1200px; height: 183px; }
  .brand-mark {
    position: absolute; left: 29px; top: 41px; width: 110px; height: 110px;
    background: linear-gradient(135deg, #6a6d70, #b9bbbd 50%, #55585b);
  }
  .brand-name {
    position: absolute; left: 165px; top: 76px;
    font-size: 32px; font-weight: 500; letter-spacing: 0.5px;
    color: var(--brand-blue); text-transform: uppercase; line-height: 1;
  }

  .city-photo {
    position: absolute; left: 0; top: 183px; width: 453px; height: 739px;
    background: linear-gradient(180deg,
      #4b5fbe 0%, #3d4fa6 18%, #2a3272 32%, #1c2040 45%,
      #121626 52%, #2c3464 60%, #1e2450 72%, #0c1130 100%);
  }

  .message-panel {
    position: absolute; left: 453px; top: 183px; width: 747px; height: 739px;
    background: var(--panel-blue);
  }
  .tagline { position: absolute; left: 56px; top: 34px; text-shadow: 2px 3px 4px rgba(0,0,0,0.35); }
  .tagline-top { font-size: 74px; font-weight: 300; line-height: 1; letter-spacing: -0.5px; }
  .tagline-small {
    position: absolute; left: 87px; top: 92px; width: 100px;
    font-size: 33px; font-weight: 300; line-height: 1.12; text-align: right;
  }
  .tagline-big {
    position: absolute; left: 199px; top: 84px;
    font-size: 98px; font-weight: 400; line-height: 1; white-space: nowrap; letter-spacing: -0.5px;
  }

  .copy {
    position: absolute; left: 58px; top: 244px; width: 632px;
    font-size: 14.2px; font-weight: 300; line-height: 18.8px; text-align: justify;
  }
  .copy p { margin-bottom: 18.8px; }
  .copy .reviewer { font-style: italic; font-weight: 400; }
  .copy .call { font-weight: 500; }

  .contact-band {
    position: absolute; left: 0; top: 785px; width: 1200px; height: 100px;
    background: var(--band-grey);
  }
  .social-list { position: absolute; left: 30px; top: 32px; display: flex; gap: 14px; list-style: none; }
  .social-list li { display: flex; align-items: center; gap: 5px; font-size: 11px; font-weight: 400; color: var(--white); }
  .social-list li::before { content: ""; width: 14px; height: 14px; background: var(--white); display: block; }

  .contact-lines {
    position: absolute; right: 178px; top: 18px; text-align: right;
    font-size: 15.5px; font-weight: 300; line-height: 21.5px; letter-spacing: 0.3px;
  }

  .agent-photo {
    position: absolute; left: 1044px; top: 769px; width: 125px; height: 125px;
    border: 3px solid var(--white);
    background: linear-gradient(160deg, #c7872e, #8d5a1f 45%, #b9c2cc 75%, #dfe3e8);
  }
</style>
</head>
<body>
<div class="ad">
  <header class="masthead">
    <div class="brand-mark"></div>
    <div class="brand-name">Voske Real Estate</div>
  </header>

  <div class="city-photo" role="img" aria-label="Night view of a domed state capitol building lit up and reflected in a river"></div>

  <section class="message-panel">
    <div class="tagline">
      <div class="tagline-top">Luxury Services</div>
      <div class="tagline-small">For All Things</div>
      <div class="tagline-big">Real Estate</div>
    </div>

    <div class="copy">
      <p>Voske Realtor? Trying to buy or sell a home? Let me work for you!</p>
      <p>See what the people are saying...</p>
      <p>In trying to buy a home from long distance, Carl went above and beyond his duty as my Realtor. His professionalism, knowledge and attentiveness were absolutely superb! What could have been a nightmare experience, turned out to be a wonderfully smooth transition. Thanks for all your help – it was truly appreciated! A++ <span class="reviewer">~ Dana Kerrow</span></p>
      <p>In this difficult sales market, I believe every effort was made to sell our home successfully. We truly appreciate the expenditure of time, energy and resources by Summit Ridge Realty and their encouragement and persistence extended in this successful outcome. <span class="reviewer">~ Tom and Lisa Harwell</span></p>
      <p>We have and will recommend Carl Voske to anyone looking to buy or sell any Real Estate. We feel Carl did an exceptional job selling our property even that it was was at the low end of the Real Estate market. <span class="reviewer">~ Mark and Jenna Ostrand</span></p>
      <p class="call">Call me today to book an appointment.</p>
    </div>
  </section>

  <footer class="contact-band">
    <ul class="social-list">
      <li>FL</li>
      <li>Chirpr</li>
      <li>Qlink</li>
      <li>Pinmosaic</li>
      <li>Vidstream</li>
    </ul>
    <div class="contact-lines">
      <div>Voske Real Estate • Carl Voske • Broker/Owner</div>
      <div>For more information call 304-555-0194 or email Carl@VoskeRealEstate.Example</div>
      <div>Visit VoskeRealEstate.Example today.</div>
    </div>
  </footer>

  <div class="agent-photo" role="img" aria-label="Portrait of the agent in front of autumn foliage"></div>
</div>
</body>
</html>
```